Lantern Care Solutions Banner Ad

Need a 750 x 250-pixel banner ad with the company Logo included. Please see company website at www.lanterncaresolutions.example for more information.

```html
<!DOCTYPE html>
<html lang="en">
<head>
<meta charset="utf-8">
<title>Lantern Care Solutions – Banner Ad</title>
<link rel="stylesheet" href="https://fonts.googleapis.com/css2?family=Exo+2:wght@700;800&family=Open+Sans:wght@300&display=swap">
<style>
  :root {
    --navy: #0f4f92;
    --navy-deep: #0a3f7a;
    --green: #74bc2a;
    --white: #ffffff;
    --stage: #e9e9e9;
    --ink-soft: #4a4a4a;
    --photo-a: #c9b79a;
    --photo-b: #6f7f8c;
  }
  * { margin: 0; padding: 0; box-sizing: border-box; }
  html, body {
    width: 975px;
    height: 1200px;
    overflow: hidden;
    background: var(--stage);
  }
  .banner {
    position: absolute;
    left: 112px;
    top: 475px;
    width: 750px;
    height: 250px;
    overflow: hidden;
    background: radial-gradient(circle at 0% 60%, #eef1f5 0%, var(--white) 45%);
    box-shadow: 0 8px 20px rgba(0,0,0,0.18);
  }
  .banner-shapes { position: absolute; inset: 0; }
  .brand {
    position: absolute;
    left: 56px;
    top: 30px;
    display: flex;
    align-items: center;
    gap: 8px;
  }
  .brand-dot {
    width: 22px;
    height: 22px;
    border-radius: 50%;
    background: var(--navy);
  }
  .brand-name {
    font-family: "Exo 2", sans-serif;
    font-weight: 800;
    font-size: 22px;
    color: var(--green);
    letter-spacing: 0.2px;
  }
  .headline {
    position: absolute;
    left: 51px;
    top: 82px;
    font-family: "Exo 2", sans-serif;
    font-weight: 700;
    font-size: 22px;
    line-height: 28px;
    color: var(--navy);
  }
  .headline strong { font-weight: 800; }
  .headline .accent { color: var(--green); font-weight: 800; }
  .subline {
    position: absolute;
    left: 51px;
    top: 167px;
    font-family: "Open Sans", sans-serif;
    font-weight: 300;
    font-size: 15px;
    color: var(--ink-soft);
  }
  .contact {
    position: absolute;
    left: 52px;
    bottom: 8px;
    display: flex;
    align-items: center;
    gap: 8px;
    font-family: "Exo 2", sans-serif;
    color: var(--white);
  }
  .contact-phone { font-size: 17px; font-weight: 800; letter-spacing: 0.5px; }
  .contact-divider { width: 1px; height: 16px; background: rgba(255,255,255,0.6); }
  .contact-web { font-size: 13px; font-weight: 700; }
  .contact-web .domain { color: var(--green); }
  .contact-icon { width: 12px; height: 12px; }
</style>
</head>
<body>
  <section class="banner">
    <svg class="banner-shapes" width="750" height="250" viewBox="0 0 750 250">
      <defs>
        <radialGradient id="photoTone" cx="50%" cy="45%" r="60%">
          <stop offset="0%" stop-color="var(--photo-a)"/>
          <stop offset="100%" stop-color="var(--photo-b)"/>
        </radialGradient>
      </defs>
      <path class="swoosh-green" d="M150,204 Q360,222 520,150 L750,0 L750,30 L530,168 Q360,232 150,210 Z" fill="var(--green)"/>
      <path class="swoosh-navy" d="M0,186 Q240,236 520,166 L750,18 L750,250 L0,250 Z" fill="var(--navy)"/>
      <circle class="photo-ring" cx="599" cy="124" r="107" fill="var(--white)" stroke="var(--green)" stroke-width="12"/>
      <circle class="photo-stitch" cx="599" cy="124" r="96" fill="none" stroke="var(--navy)" stroke-width="1" stroke-dasharray="2 2"/>
      <circle class="photo" cx="599" cy="124" r="93" fill="url(#photoTone)" role="img" aria-label="Photo of a young woman in a wheelchair reading a tablet in a bright workspace"/>
    </svg>

    <div class="brand">
      <span class="brand-dot"></span>
      <span class="brand-name">Lantern Care Solutions</span>
    </div>

    <h1 class="headline">
      <strong>DDD Eligibility Requirements</strong><br>
      in <span class="accent">New Jersey</span> for Adults with<br>
      Special Needs
    </h1>
    <p class="subline">Special Needs Students’ Transition to Adulthood</p>

    <div class="contact">
      <svg class="contact-icon" viewBox="0 0 24 24"><path d="M6.6 10.8a15.1 15.1 0 0 0 6.6 6.6l2.2-2.2a1 1 0 0 1 1-.25 11.4 11.4 0 0 0 3.6.57 1 1 0 0 1 1 1V20a1 1 0 0 1-1 1A17 17 0 0 1 3 4a1 1 0 0 1 1-1h3.5a1 1 0 0 1 1 1c0 1.25.2 2.45.57 3.57a1 1 0 0 1-.25 1z" fill="var(--white)"/></svg>
      <span class="contact-phone">555-010-4827</span>
      <span class="contact-divider"></span>
      <svg class="contact-icon" viewBox="0 0 24 24" fill="none" stroke="var(--white)" stroke-width="2"><circle cx="12" cy="12" r="10"/><path d="M2 12h20M12 2c3 3 3 17 0 20M12 2c-3 3-3 17 0 20"/></svg>
      <span class="contact-web">www.<span class="domain">lanterncaresolutions</span>.example</span>
    </div>
  </section>
</body>
</html>
```